Menu Design Project

We are a post colonial tavern serving craft beer, local wine and fine spirits. Our colors are black, copper and old brick. We are on a town square,...

Town

```html
<!DOCTYPE html>
<html lang="en">
<head>
<meta charset="utf-8">
<title>Harlow's Tavern Menu</title>
<link href="https://fonts.googleapis.com/css2?family=EB+Garamond:ital,wght@0,400;0,500;0,600;1,400&display=swap" rel="stylesheet">
<style>
:root{
  --page:#ffffff;
  --panel:#2c2b2a;
  --panel-edge:#3a3836;
  --copper:#a8845a;
  --copper-light:#c0a07a;
  --body-text:#bfb09a;
  --desc:#a79c8e;
  --rule:#8a6c4b;
  --brick-1:#7b3a25;
  --brick-2:#5a2c1f;
  --brick-3:#2e211d;
  --logo:#f3efe8;
}
*{box-sizing:border-box;margin:0;padding:0}
html,body{width:1200px;height:1000px;overflow:hidden;background:var(--page)}
body{position:relative;font-family:"EB Garamond",serif;color:var(--body-text)}

.spread{position:absolute;left:298px;width:604px;overflow:hidden;background:var(--panel)}
.spread--outside{top:28px;height:467px}
.spread--inside{top:504px;height:466px}

.brick{position:absolute;top:0;height:100%;
  background:radial-gradient(ellipse at 50% 45%,var(--brick-1) 0%,var(--brick-2) 55%,var(--brick-3) 100%)}
.brick--back{left:0;width:149px}
.brick--front{left:325px;width:279px}

.wordmark{position:absolute;color:var(--logo);font-weight:600;line-height:1;white-space:nowrap;text-align:center}
.wordmark__name{display:block;font-size:58px}
.wordmark__sub{display:block;font-size:11px;letter-spacing:4px;margin-top:2px}
.wordmark--back{left:-60px;top:112px}
.wordmark--front{left:528px;top:112px}

.column{position:absolute;top:0;height:100%;background:var(--panel)}
.column--center{left:149px;width:176px;padding:0 10px}

.sec{position:absolute;left:10px;right:10px}
.sec-title{color:var(--copper);font-size:15px;font-weight:500;text-align:center;letter-spacing:.5px;line-height:1;white-space:nowrap}
.sec-title--left{text-align:left}
.sec-title--wide{letter-spacing:0;font-size:14.5px}
.sec-note{font-size:5.2px;text-transform:uppercase;text-align:center;color:var(--body-text);line-height:1.35;margin-top:3px;letter-spacing:.2px}
.rule{position:absolute;left:10px;right:22px;height:1px;background:var(--rule)}

.row{display:flex;align-items:baseline;color:var(--copper);font-size:8.6px;line-height:11.5px;white-space:nowrap}
.dots{flex:1;border-bottom:1px dotted var(--copper);margin:0 1px;transform:translateY(-2px);opacity:.7}
.price{font-size:8.6px}
.price--market{font-size:5.5px}
.desc{font-style:italic;font-size:5.4px;line-height:7px;color:var(--desc);white-space:nowrap}
.addon{font-size:5.4px;line-height:7px;color:var(--copper)}
.bev{font-size:9px;line-height:11px;color:var(--copper);white-space:nowrap}
.disclaimer{font-size:5.1px;text-transform:uppercase;line-height:7px;color:var(--desc);white-space:nowrap}

.col{position:absolute;top:0;height:100%;background:var(--panel)}
.col--starters{left:0;width:151px}
.col--mains{left:154px;width:296px}
.col--greens{left:454px;width:150px}
.divider{position:absolute;top:0;width:3px;height:100%;background:var(--panel-edge)}
.divider--a{left:151px}
.divider--b{left:450px}
.col .sec{left:11px;right:9px}
.col--mains .sec{left:9px;right:9px}
.col .sec.sec--heading{left:3px;right:3px}
.hrule{position:absolute;left:8px;right:8px;height:1px;background:var(--rule)}
</style>
</head>
<body>

<section class="spread spread--outside">
  <div class="brick brick--back" role="img" aria-label="Red brick wall photograph"></div>
  <div class="wordmark wordmark--back"><span class="wordmark__name">Harlow's</span><span class="wordmark__sub">TAVERN</span></div>

  <div class="column column--center">
    <div class="sec" style="top:9px">
      <h2 class="sec-title">KIDS</h2>
      <p class="sec-note">All kids meals served with<br>your choice of side item</p>
    </div>
    <div class="sec" style="top:51px">
      <div class="row">Chicken Tenders<span class="dots"></span><span class="price">8</span></div>
      <div class="row">Corndog<span class="dots"></span><span class="price">6</span></div>
      <div class="row">Grilled Cheese<span class="dots"></span><span class="price">5</span></div>
    </div>
    <div class="rule" style="top:96px"></div>

    <div class="sec" style="top:108px"><h2 class="sec-title">SIDES</h2></div>
    <div class="sec" style="top:126px">
      <div class="row">Creole Seasoned Fries<span class="dots"></span><span class="price">2</span></div>
      <div class="row">Sweet Potato Fries<span class="dots"></span><span class="price">2</span></div>
      <div class="row">Rice Pilaf<span class="dots"></span><span class="price">2</span></div>
      <div class="row">Broccoli<span class="dots"></span><span class="price">2</span></div>
      <div class="row">Onion Rings<span class="dots"></span><span class="price">2</span></div>
      <div class="row">Side Salad<span class="dots"></span><span class="price">3</span></div>
    </div>
    <div class="rule" style="top:204px"></div>

    <div class="sec" style="top:216px"><h2 class="sec-title">DESSERT</h2></div>
    <div class="sec" style="top:237px">
      <div class="row">Southern Deep-Fried Cream Cakes<span class="dots"></span><span class="price">8</span></div>
      <p class="desc">Two cream cakes, deep fried and glazed with banana icing<br>and a scoop of vanilla bean ice cream.</p>
    </div>
    <div class="sec" style="top:270px">
      <div class="row">Cookie Ice Cream Sandwich<span class="dots"></span><span class="price">7</span></div>
      <p class="desc">A warm, melted macadamia nut cookie served hot with<br>a scoop of vanilla bean ice cream and sprinkled with<br>coconut, whipped cream and cherry.</p>
    </div>
    <div class="sec" style="top:310px">
      <div class="row">Chattanooga Deep-Fried Marshmallow Pie<span class="dots"></span><span class="price">8</span></div>
      <p class="desc">Chocolate or vanilla marshmallow pie deep-fried and topped with<br>vanilla bean ice cream, whipped cream and a cherry.</p>
    </div>
    <div class="rule" style="top:347px"></div>

    <div class="sec" style="top:362px">
      <div class="row"><h2 class="sec-title sec-title--left">BEVERAGES</h2><span class="dots"></span><span class="price">2</span></div>
      <p class="bev">Cola / Diet Cola / Lemon-Lime /<br>Pepper Soda / Lemonade / Sweet Tea /<br>Unsweet Tea / Coffee</p>
    </div>

    <div class="sec" style="top:441px;left:6px;right:4px">
      <p class="disclaimer">*Consuming raw or undercooked meats, poultry,<br>seafood, shellfish, or eggs may increase your risk<br>of foodborne illness.</p>
    </div>
  </div>

  <div class="brick brick--front" role="img" aria-label="Red brick wall photograph"></div>
  <div class="wordmark wordmark--front"><span class="wordmark__name">Harlow's</span><span class="wordmark__sub">TAVERN</span></div>
</section>

<section class="spread spread--inside">
  <div class="col col--starters">
    <div class="sec sec--heading" style="top:6px"><h2 class="sec-title sec-title--wide">HORS D'OEUVRES</h2></div>
    <div class="sec" style="top:28px">
      <div class="row">Calamari<span class="dots"></span><span class="price">9</span></div>
      <p class="desc">Tender squid lightly floured then deep-fried, served<br>with fresh lemon wedges and marinara sauce.</p>
    </div>
    <div class="sec" style="top:61px">
      <div class="row">Coconut Shrimp<span class="dots"></span><span class="price">9</span></div>
      <p class="desc">Six jumbo shrimp battered in coconut flakes then<br>deep-fried, served with fresh lemon wedges and<br>sweet chili sauce.</p>
    </div>
    <div class="sec" style="top:100px">
      <div class="row">Cajun Shrimp Nuggets<span class="dots"></span><span class="price">10</span></div>
      <p class="desc">Several gulf shrimp battered in our homemade<br>Cajun seasoning then deep-fried, served with<br>fresh lemon wedges our Remoulade sauce.</p>
    </div>
    <div class="sec" style="top:141px">
      <div class="row">Southwest Shrimp Skewers<span class="dots"></span><span class="price">10</span></div>
      <p class="desc">6 gulf shrimp grilled to perfection in garlic and<br>butter, topped with homemade Pico De Gallo and<br>fresh lemon wedges.</p>
    </div>
    <div class="sec" style="top:181px">
      <div class="row">Chicken Wings<span class="dots"></span><span class="price">10</span></div>
      <p class="desc">Marinated chicken wings deep-fried then<br>hand-tossed into your choice of our homemade<br>buffalo sauce, honey barbeque sauce, Honey<br>Chipotle or served naked with freshly cut carrots,<br>celery and your choice of sauce.</p>
    </div>
    <div class="sec" style="top:235px">
      <div class="row">Deep-Fried Pickles<span class="dots"></span><span class="price">8</span></div>
      <p class="desc">A generous portion of pickles tossed in our<br>signature batter then deep-fried, served with<br>a ranch sauce.</p>
    </div>
    <div class="sec" style="top:275px">
      <div class="row">Mozzarella Sticks<span class="dots"></span><span class="price">8</span></div>
      <p class="desc">Mozzarella cheese seasoned with Italian herbs<br>then deep-fried and served with marinara sauce.</p>
    </div>
    <div class="sec" style="top:308px">
      <div class="row">Chips &amp; Pico<span class="dots"></span><span class="price">7</span></div>
      <p class="desc">Fresh corn tortilla chips with fresh homemade<br>Pico De Gallo.</p>
    </div>
    <div class="sec" style="top:341px">
      <div class="row">Fried Green Tomatoes<span class="dots"></span><span class="price">8</span></div>
      <p class="desc">Vine ripe fried green tomatoes with a Pimento<br>Cheese base and sprinkled with bacon.</p>
    </div>
    <div class="sec" style="top:374px">
      <div class="row">Loaded Southwest Fries<span class="dots"></span><span class="price">10</span></div>
      <p class="desc">Creole seasoned fries layered with cheddar and<br>parmesan, topped with Pico De Gallo, homemade<br>Remoulade and Ranch.</p>
      <p class="addon">Add Chicken-$3**<br>Add Steak-$5**</p>
      <p class="desc" style="font-style:normal;color:var(--body-text)">**NOT INCLUDED IN TRIO PRICE</p>
    </div>
    <div class="sec" style="top:435px">
      <div class="row">Harlow's Signature Trio<span class="dots"></span><span class="price">20</span></div>
      <p class="desc">Choose any of the above three full portioned fresh<br>Hors D'ouevres.</p>
    </div>
  </div>

  <div class="divider divider--a"></div>

  <div class="col col--mains">
    <div class="sec" style="top:6px">
      <h2 class="sec-title" style="font-size:15.5px">ENTRÉES</h2>
      <p class="sec-note">All entrées served with your choice of side item</p>
    </div>
    <div class="sec" style="top:58px">
      <div class="row">Tavern BLT<span class="dots"></span><span class="price">6</span></div>
      <p class="desc">Tennessee bacon cooked to perfection served with a fresh tomato slice, lettuce and mayo spread on<br>sourdough bread mayonnaise.</p>
      <p class="addon">Add Fried Green Tomatoes-$2</p>
    </div>
    <div class="sec" style="top:96px">
      <div class="row">Cajun Shrimp Po'boy<span class="dots"></span><span class="price">12</span></div>
      <p class="desc">Cajun breaded gulf shrimp served on a Hoagie Bun with fresh tomatoes, lettuce and mayo. Covered with<br>a Cajun Remoulade sauce and sprinkled with Creole seasoning.</p>
    </div>
    <div class="sec" style="top:131px">
      <div class="row">Buttermilk Battered Chicken Tenders<span class="dots"></span><span class="price">12</span></div>
      <p class="desc">Three huge chicken tenders, breaded and battered then hand-tossed into your choice of our homemade<br>buffalo sauce, honey barbeque sauce, Honey Chipotle or served regular with your choice of sauce.</p>
    </div>
    <div class="sec" style="top:163px">
      <div class="row">Harlow's Famous Reuben Sandwich<span class="dots"></span><span class="price">10</span></div>
      <p class="desc">Corned beef, Provolone cheese and sauerkraut served on rye bread with signature dressing.</p>
    </div>
    <div class="sec" style="top:189px">
      <div class="row">Philly Cheesesteak<span class="dots"></span><span class="price">10</span></div>
      <p class="desc">Mouthwatering philly cheesesteak grilled with peppers and onions with our signature dressing.</p>
    </div>
    <div class="sec" style="top:215px">
      <div class="row">Chicken Sandwich<span class="dots"></span><span class="price">10</span></div>
      <p class="desc">Grilled or fried chicken breast served on a Kaiser Bun with lettuce, tomato and mayo. Hand-tossed in your<br>choice of our homemade buffalo sauce, honey barbeque sauce, Honey Chipotle or served naked with freshly<br>cut carrots, celery and your choice of sauce.</p>
    </div>
    <div class="sec" style="top:253px">
      <div class="row">Caribbean Grouper Sandwich<span class="dots"></span><span class="price">14</span></div>
      <p class="desc">Caribbean grouper grilled or fried, served on a Kaiser Roll with lettuce, tomato and mayo.</p>
    </div>
    <div class="sec" style="top:280px">
      <div class="row">B&amp;B Steak and Onions*<span class="dots"></span><span class="price">14</span></div>
      <p class="desc">Shoulder top blade steak cooked to your preference. Topped with sauteed onions, crispy bacon bits and<br>bleu cheese crumbles.</p>
    </div>
    <div class="sec" style="top:313px">
      <div class="row">Harlow's Signature Tavern Burger*<span class="dots"></span><span class="price">10</span></div>
      <p class="desc">Our fresh, never frozen burgers are 100% Black Angus Beef and are made to perfection with your choice<br>of cheddar, Swiss, American or Provolone Cheese, juicy bacon, your choices of ketchup, mustard or mayo<br>served on a bun with your choices of tomato, lettuce and onion.</p>
    </div>
    <div class="sec" style="top:356px">
      <div class="row">Veracruz Quesadilla<span class="dots"></span><span class="price">7</span></div>
      <p class="desc">Wheat tortilla grilled with melted cheese, onions and jalapeno peppers with a side of Pico De Gallo<br>and sour cream.</p>
      <p class="addon">Add Chicken-$3<br>Add Steak or Shrimp-$5</p>
    </div>
    <div class="sec" style="top:404px">
      <div class="row">River City Nachos<span class="dots"></span><span class="price">11</span></div>
      <p class="desc">Fresh corn tortilla chips with fresh homemade Pico De Gallo, melted cheese, onions, jalepeno peppers.</p>
      <p class="addon">Add Chicken-$3<br>Add Steak or Shrimp-$5</p>
    </div>
  </div>

  <div class="divider divider--b"></div>

  <div class="col col--greens">
    <div class="sec sec--heading" style="top:6px"><h2 class="sec-title" style="font-size:15px">FRESH GREENS</h2></div>
    <div class="sec" style="top:37px">
      <div class="row">House Salad<span class="dots"></span><span class="price">9</span></div>
      <p class="desc">A generous portion of Iceberg &amp; Romaine lettuce<br>with fresh diced tomatoes, onions and carrots with<br>your choice of ranch, bleu cheese, Italian or<br>balsamic vinaigrette dressing.</p>
    </div>
    <div class="sec" style="top:83px">
      <div class="row">Caesar Salad<span class="dots"></span><span class="price">8</span></div>
      <p class="desc">A generous portion of Romaine lettuce sprinkled<br>with parmesan cheese, croutons with a side of<br>Caesar dressing.</p>
      <p class="addon">Add Grilled or Fried Chicken-$3<br>Add Steak* or Shrimp-$5</p>
    </div>
    <div class="hrule" style="top:154px"></div>

    <div class="sec" style="top:172px">
      <h2 class="sec-title" style="font-size:15px">WRAPS</h2>
      <p class="sec-note">Served with your choice of side item</p>
    </div>
    <div class="sec" style="top:209px">
      <div class="row">Veggie Wrap<span class="dots"></span><span class="price">8</span></div>
      <p class="desc">Romaine and Iceberg lettuce, onions and tomato<br>wrapped in a wheat tortilla with the dressing of<br>your choice.</p>
      <p class="addon">Add Grilled or Fried Chicken-$3<br>Add Steak*, Grouper or Shrimp-$5</p>
    </div>
    <div class="hrule" style="top:273px"></div>

    <div class="sec sec--heading" style="top:296px"><h2 class="sec-title" style="font-size:15px">FRESH CATCH</h2></div>
    <div class="sec" style="top:321px">
      <div class="row">Garlic Buttered Scallops<span class="dots"></span><span class="price price--market">Market Price</span></div>
      <p class="desc">Three fresh scallops grilled to perfection in butter<br>and served with a side of garlic butter.</p>
    </div>
    <div class="sec" style="top:354px">
      <div class="row">Fresh Fish of the Day!<span class="dots"></span><span class="price price--market">Market Price</span></div>
      <p class="desc">Ask about the fish of the day, brought in fresh and<br>served to perfection. Seasons vary for Amberjack,<br>Chilean Seabass, Black Grouper, Mahi, Redfish,<br>Red Snapper, Swordfish, Tuna or Canadian Salmon.</p>
    </div>
    <div class="sec" style="top:401px">
      <div class="row">Surf and Turf*<span class="dots"></span><span class="price price--market">Market Price</span></div>
      <p class="desc">Fresh catch of the day, grilled in buttered<br>seasoning and served along with an eight ounce<br>shoulder top blade steak covered in onions.</p>
    </div>
  </div>
</section>

</body>
</html>
```